Bramwell Business Cards

Logo files are included. Full "Bramwell" logo should be included on the back of the business card. The B symbol should be included on the front with the contact information.

Bramwell, LLC is the company name and we do commercial construction and real estate development consulting services. Look for a fairly simple card design utilizing our logo.

```html
<!DOCTYPE html>
<html lang="en">
<head>
<meta charset="utf-8">
<title>Bramwell Business Cards</title>
<link href="https://fonts.googleapis.com/css2?family=Roboto:wght@400;500&display=swap" rel="stylesheet">
<style>
  :root {
    --backdrop: #2c2c2c;
    --card: #183247;
    --card-deep: #132a3c;
    --emboss: #112536;
    --emboss-light: #24435b;
    --gold: #d99a1a;
    --ink: #e9edf1;
    --ink-soft: #d4dbe2;
  }
  * { margin: 0; padding: 0; box-sizing: border-box; }
  html, body {
    width: 1200px; height: 1138px; overflow: hidden;
    background: var(--backdrop);
    font-family: "Roboto", Arial, sans-serif;
  }
  .canvas { position: relative; width: 1200px; height: 1138px; }
  .card {
    position: absolute;
    width: 620px; height: 375px;
    border-radius: 16px;
    background: linear-gradient(160deg, var(--card) 0%, var(--card-deep) 100%);
  }
  .card--front { left: 272px; top: 184px; }
  .card--back { left: 275px; top: 606px; }

  /* front: embossed brand mark */
  .front-mark {
    position: absolute; left: 181px; top: 58px;
    width: 264px; height: 264px;
    border-radius: 50%;
    border: 3px solid var(--emboss);
    box-shadow: 0 1px 0 var(--emboss-light), inset 0 1px 0 var(--emboss-light);
    display: flex; align-items: center; justify-content: center;
  }
  .front-name {
    font-size: 32px; font-weight: 500; letter-spacing: 2px;
    line-height: 1;
    color: var(--emboss);
    text-shadow: 0 1px 0 var(--emboss-light);
  }

  /* back: brand block */
  .brand-circle {
    position: absolute; left: 424px; top: 58px;
    width: 80px; height: 80px; border-radius: 50%;
    border: 4px solid var(--gold);
  }
  .brand-name {
    position: absolute; right: 30px; top: 140px;
    font-size: 44px; font-weight: 500; letter-spacing: 1px;
    color: var(--ink); line-height: 1;
  }

  .person-name {
    position: absolute; left: 27px; top: 204px;
    font-size: 25px; font-weight: 500; color: var(--gold);
  }
  .person-title {
    position: absolute; left: 27px; top: 236px;
    font-size: 16px; color: var(--ink-soft);
  }
  .divider { position: absolute; left: 0; top: 260px; }

  .contact-list {
    position: absolute; left: 32px; top: 284px;
    list-style: none;
  }
  .contact-list li {
    display: flex; align-items: center;
    height: 23.5px;
    font-size: 16px; color: var(--ink-soft);
  }
  .contact-list svg { width: 16px; height: 16px; margin-right: 10px; }

  .address {
    position: absolute; right: 30px; top: 308px;
    text-align: right;
    font-size: 16px; line-height: 23.5px; color: var(--ink-soft);
  }
</style>
</head>
<body>
<div class="canvas">

  <section class="card card--front">
    <div class="front-mark">
      <div class="front-name">BRAMWELL</div>
    </div>
  </section>

  <section class="card card--back">
    <div class="brand-circle"></div>
    <div class="brand-name">BRAMWELL</div>

    <div class="person-name">Alden Pryce</div>
    <div class="person-title">Managing Director</div>

    <svg class="divider" width="620" height="30" viewBox="0 0 620 30">
      <path d="M27 9 H228 C258 9 262 27 290 27 H590" fill="none" stroke="var(--gold)" stroke-width="1.4"/>
    </svg>

    <ul class="contact-list">
      <li>
        <svg viewBox="0 0 16 16"><path d="M2 6 C2 3 14 3 14 6 L11.5 7 L10.5 5.5 H5.5 L4.5 7 Z M4 8 H12 L13 13 H3 Z" fill="var(--gold)"/></svg>
        555-204-7731
      </li>
      <li>
        <svg viewBox="0 0 16 16"><rect x="1" y="3.5" width="14" height="9" fill="var(--gold)"/><path d="M1 3.5 L8 9 L15 3.5" fill="none" stroke="var(--card)" stroke-width="1.2"/></svg>
        alden@bramwell.com
      </li>
      <li>
        <svg viewBox="0 0 16 16"><circle cx="8" cy="8" r="6.5" fill="none" stroke="var(--gold)" stroke-width="1.4"/><ellipse cx="8" cy="8" rx="2.8" ry="6.5" fill="none" stroke="var(--gold)" stroke-width="1.2"/><path d="M1.5 8 H14.5 M2.5 5 H13.5 M2.5 11 H13.5" stroke="var(--gold)" stroke-width="1.1"/></svg>
        www.bramwell.com
      </li>
    </ul>

    <div class="address">418 Ledger Ave., Fairview,<br>Millbrook, US 204518</div>
  </section>

</div>
</body>
</html>
```